Attention Getting Doorhanger Postcard Campaign offering HUGE Rebate on New Construction Homes

I am reestablishing my real estate career in the far North Dallas, TX area and want to offer a rebate on new construction homes to help get me started. I am requesting a doorhanger as my first project but would like a theme that I can carry over to other projects including postcards and other marketing items. I want it to look high end, clean, professional and classy. I am attaching a copy of a flier that I created that needs (no graphic designer here) some prettying up. But this is just to give you an idea of the type of style that is of interest to me.

Target Market(s)

Home buyers for new construction in far north dallas suburbs. Usually a move up buyer.

Industry/Entity Type

Real Estate

Colors

Designer to choose colors to be used in the design.

Requirements
Must have
• Catch phrase, draw attention, classy clean lines, current trend colors of blues and grays. My information, Harwood Fenn logo, equal housing and realtor logos. Fine Print: Not intended to solicit homes already listed for sale or buyers already in a buyers agency agreement with another brokerage. Please include offer details as listed in my flier. Again I am interested in a door hanger and the next round would be a flier or postcard.
Nice to have
• Picture of new homes that are in line with what is being built in my area. A few home builders sites: Silver Meadow, Brookvale Homes, Tenbury Homes, Calloway Homes.

```html
<!DOCTYPE html>
<html lang="en">
<head>
<meta charset="utf-8">
<title>Door Hanger – New Construction Rebate</title>
<link href="https://fonts.googleapis.com/css2?family=Open+Sans:wght@400;600;700;800&family=Kaushan+Script&family=Allura&family=Patrick+Hand+SC&display=swap" rel="stylesheet">
<style>
:root{
  --bg:#d2d3d5;
  --slate:#5f5f5f;
  --sky:#b9d3ec;
  --ink:#000;
  --paper:#fff;
  --text:#222;
  --link:#1f4e8c;
  --brand:#b5121b;
  --muted:#555;
}
*{box-sizing:border-box;margin:0;padding:0}
html,body{width:1200px;height:1117px;overflow:hidden;background:var(--bg);font-family:"Open Sans",sans-serif}
.hanger{position:absolute;top:132px;width:360px;height:887px;overflow:hidden;background:var(--paper)}
.hanger--front{left:142px}
.hanger--back{left:527px}
.band{position:absolute;left:0;width:100%}
.hole{position:absolute;left:0;top:0}
/* front */
.front-top{top:0;height:359px;background:var(--slate)}
.headline{position:absolute;left:0;top:0;width:100%;height:359px;color:var(--sky);line-height:1;font-weight:800}
.headline span{position:absolute;white-space:nowrap}
.headline .awe{left:38px;top:254px;font-size:51px}
.headline .then{left:171px;top:258px;font-size:21px;font-weight:600}
.headline .some{left:166px;top:278px;font-size:51px}
.photo{top:359px;height:216px;background:linear-gradient(180deg,#c9aeb8 0%,#d8d4dc 35%,#8a8f8e 62%,#4d6a3a 100%)}
.offer{top:575px;height:128px;background:var(--ink);color:var(--paper);font-family:"Patrick Hand SC",cursive;text-align:center;font-size:20px;letter-spacing:1.5px;line-height:31px;padding-top:18px}
.offer .hi{color:var(--sky)}
.offer .big{font-size:25px}
.agent{top:703px;height:184px;background:var(--paper)}
.agent-ring{position:absolute;left:26px;top:27px}
.agent-photo{position:absolute;left:38px;top:39px;width:104px;height:104px;border-radius:50%;background:radial-gradient(circle at 50% 40%,#b98a72,#5a3b32 70%,#2d2424)}
.agent-name{position:absolute;left:168px;top:38px;font-family:"Allura",cursive;font-size:31px;line-height:1.1;color:var(--text)}
.agent-creds{position:absolute;left:168px;top:74px;font-size:8.5px;font-weight:600;color:var(--text)}
.contact{position:absolute;left:168px;font-size:12px;line-height:16px;color:var(--text);display:flex;align-items:center;gap:8px}
.contact--phone{top:106px}
.contact--mail{top:127px;color:var(--link);font-size:11px}
/* back */
.back-top{top:0;height:418px;background:var(--slate)}
.points{position:absolute;left:38px;top:231px;list-style:none;color:var(--paper);font-size:9.4px;font-weight:700;line-height:14px}
.points li{border-left:2.5px solid var(--paper);padding-left:9px;margin-bottom:18px}
.points li:nth-child(3){margin-bottom:13px}
.example{top:418px;height:106px;background:var(--sky);text-align:center;color:var(--ink)}
.example h3{font-family:"Kaushan Script",cursive;font-size:17px;font-weight:400;margin-top:6px}
.example-row{display:flex;justify-content:center;align-items:center;gap:10px;margin-top:2px;font-size:14px;line-height:24px}
.example-row b{font-weight:700;font-size:15px}
.example-row .divider{width:3px;height:40px;background:var(--ink)}
.example small{display:block;font-size:11px;margin-top:4px}
.savings{top:524px;height:121px;background:var(--ink);color:var(--paper);text-align:center;line-height:26px;font-size:13px;padding-top:8px}
.savings h3{font-family:"Kaushan Script",cursive;font-size:20px;font-weight:400}
.savings .pkg{color:var(--sky);font-weight:700;font-size:16px;border-bottom:1.5px solid var(--paper)}
.savings .hi{color:var(--sky);font-weight:700;font-size:16px}
.steps{position:absolute;left:0;top:648px}
.steps-title{position:absolute;left:16px;top:10px;font-size:11.5px;color:#333}
.step-label{position:absolute;font-size:7.5px;color:#333;text-align:center;line-height:10px}
.note{position:absolute;left:19px;top:762px;width:330px;font-size:9.6px;line-height:13px;color:var(--text)}
.note .sign{display:block;text-align:right;margin-right:12px}
.brand{position:absolute;left:60px;top:824px;display:flex;align-items:center;gap:6px}
.brand-name{font-size:14px;font-weight:400;color:var(--muted);letter-spacing:.5px;line-height:18px}
.brand-mark{width:12px;height:12px;background:var(--brand)}
.brand-note{position:absolute;left:70px;top:852px;font-size:9.5px;color:#888}
.badge{position:absolute;top:824px;width:18px;height:20px;background:#222}
</style>
</head>
<body>

<section class="hanger hanger--front">
  <div class="band front-top"></div>
  <svg class="hole" width="360" height="200" viewBox="0 0 360 200" aria-hidden="true">
    <path d="M0 111 C50 111 95 110 125 96 L140 178 C105 166 55 161 0 161 Z" fill="var(--bg)"/>
    <circle cx="180" cy="128" r="63" fill="var(--bg)"/>
  </svg>
  <h1 class="headline">
    <span class="awe">AWE</span><span class="then">and then</span><span class="some">SOME</span>
  </h1>
  <div class="band photo" role="img" aria-label="Photo of a white two-story new construction home with a dark roof at dusk"></div>
  <div class="band offer">
    <p>Receive a minimum of <span class="hi big">2.5%</span></p>
    <p>or more to put towards</p>
    <p class="hi">your new construction home!</p>
  </div>
  <div class="band agent">
    <svg class="agent-ring" width="128" height="128" viewBox="0 0 128 128" aria-hidden="true">
      <path d="M64 4 A60 60 0 1 1 10 92" fill="none" stroke="#555" stroke-width="5"/>
      <path d="M4 64 A60 60 0 0 1 40 9" fill="none" stroke="#999" stroke-width="5"/>
    </svg>
    <div class="agent-photo" role="img" aria-label="Portrait photo of the agent"></div>
    <p class="agent-name">Dana Whitlock</p>
    <p class="agent-creds">REALTOR®, CRS, ABR, CNHS, CHMS</p>
    <p class="contact contact--phone">
      <svg width="10" height="11" viewBox="0 0 24 24" aria-hidden="true"><path d="M6.6 10.8a15 15 0 0 0 6.6 6.6l2.2-2.2a1 1 0 0 1 1-.25 11.4 11.4 0 0 0 3.6.57 1 1 0 0 1 1 1V20a1 1 0 0 1-1 1A17 17 0 0 1 3 4a1 1 0 0 1 1-1h3.5a1 1 0 0 1 1 1c0 1.25.2 2.45.57 3.57a1 1 0 0 1-.25 1z" fill="#222"/></svg>
      469.555.0174
    </p>
    <p class="contact contact--mail">
      <svg width="10" height="10" viewBox="0 0 20 20" aria-hidden="true"><circle cx="10" cy="10" r="8.5" fill="none" stroke="#333" stroke-width="2"/><ellipse cx="10" cy="10" rx="3.5" ry="8.5" fill="none" stroke="#333" stroke-width="1.5"/><path d="M1.5 10h17" stroke="#333" stroke-width="1.5"/></svg>
      danawhitlock@mailbox.com
    </p>
  </div>
</section>

<section class="hanger hanger--back">
  <div class="band back-top"></div>
  <svg class="hole" width="360" height="200" viewBox="0 0 360 200" aria-hidden="true">
    <path d="M360 111 C310 111 265 110 235 96 L220 178 C255 166 305 161 360 161 Z" fill="var(--bg)"/>
    <circle cx="180" cy="128" r="63" fill="var(--bg)"/>
  </svg>
  <ul class="points">
    <li>We work with 100's of builders in the local area so<br>you are not limited to a few “select” builders.</li>
    <li>Homebuilders have the same bottom line sales price<br>whether you have a REALTOR® representing you or not.</li>
    <li>Rebate program will not affect the price you pay for<br>your home. Brokerage fees are paid through a separate<br>marketing fund, not from the sales price of your home.</li>
    <li>Rebate program is in ADDITION to any builder or<br>lender incentives.</li>
  </ul>
  <div class="band example">
    <h3>For Example:</h3>
    <div class="example-row">
      <p><b>$400,000</b> equals a<br><b>$10,000</b> rebate!</p>
      <span class="divider"></span>
      <p><b>$500,000</b> equals a<br><b>$12,500</b> rebate!</p>
    </div>
    <small>*Lender approval required.</small>
  </div>
  <div class="band savings">
    <h3>Maximize Your Savings!</h3>
    <p>My <span class="pkg">Buy &amp; List</span> package offers a</p>
    <p><span class="hi">FLAT FEE</span> on the sale of your current home.</p>
    <p>Saving you <span class="hi">THOUSANDS!</span></p>
  </div>
  <div class="steps">
    <p class="steps-title">How it works:</p>
    <svg width="360" height="100" viewBox="0 0 360 100" aria-hidden="true">
      <path d="M0 44 C30 44 55 68 83 68 C105 68 112 40 129 40 C150 40 155 66 172 64 C182 62 183 40 195 40 C230 38 240 70 280 68 C300 67 315 56 326 55" fill="none" stroke="#111" stroke-width="2.2"/>
      <g fill="#fff" stroke="#7ea4cc" stroke-width="1.5">
        <circle cx="83" cy="68" r="5"/><circle cx="129" cy="40" r="5"/><circle cx="195" cy="40" r="5"/><circle cx="326" cy="55" r="5"/>
      </g>
    </svg>
    <p class="step-label" style="left:60px;top:78px">Contact Dana<br>to register</p>
    <p class="step-label" style="left:108px;top:14px">Find your<br>New Home</p>
    <p class="step-label" style="left:192px;top:60px;text-align:left">Sign your<br>Contract</p>
    <p class="step-label" style="left:257px;top:32px">Close and Receive<br>your <b>REBATE!</b></p>
  </div>
  <p class="note">I've sold hundreds of homes in the North Dallas area over the last 13 years, specializing in new construction homes. I would love to help you make your new home dreams a reality.<span class="sign">Dana</span></p>
  <div class="brand"><span class="brand-mark"></span><span class="brand-name">HARWOOD FENN</span></div>
  <p class="brand-note">Each Office Is Independently Owned and Operated</p>
  <span class="badge" style="left:226px"></span>
  <span class="badge" style="left:256px"></span>
</section>

</body>
</html>
```